High Quality Business card for Property Management Agency - Super Classy and professional design

High Quality Business card design.

We need a business card designed for our Property Management Agency.
We are located on Sydney's Northern Beaches and manage beautiful properties along the beach and harbor.
We need a design that oozes modern, classy and professional.
I would like it to be double sided with contact details and logo on the front and just the logo on the back.

I need a print ready PDF version of the file as well as an editable photoshop (PSD) version of the file.

Logo and information details attached.

Target Market(s)

Property owners/investors, Male and Female Aged 28-65

Industry/Entity Type

Real Estate

Contact Information for Business Card

Tom Harlow
Tel: 0437 216 590
Email: tom@harlowestates.com.au
Website: www.harlowestates.com.au
Address: Level 2, 17 Kestrel Rd, Wendale NSW 2081

Font styles to use
Sans Serif

Requirements
Must have
• - Logo front and back
• - Business card details listed above and attached
• - Colour
Nice to have
• Sleek and professional

```html
<!DOCTYPE html>
<html lang="en">
<head>
<meta charset="utf-8">
<title>Harlow Estates – Business Card</title>
<link rel="stylesheet" href="https://fonts.googleapis.com/css2?family=Montserrat:wght@400;500;700;800&display=swap">
<style>
  :root {
    --page-bg: #3a3b3d;
    --card-black: #111315;
    --teal: #17889a;
    --teal-dark: #0f6f7e;
    --white: #ffffff;
    --soft-white: #e9ecee;
  }
  * { box-sizing: border-box; margin: 0; padding: 0; }
  html, body { width: 1200px; height: 900px; overflow: hidden; }
  body {
    background: var(--page-bg);
    font-family: "Montserrat", Arial, sans-serif;
    position: relative;
  }
  .card {
    position: absolute;
    left: 250px;
    width: 700px;
    height: 400px;
    background: var(--card-black);
    border-radius: 24px;
    overflow: hidden;
  }
  .card--back { top: 40px; }
  .card--front { top: 465px; }
  .card-bands { position: absolute; inset: 0; }

  /* Back */
  .back-brand {
    position: absolute;
    left: 0; right: 0; top: 140px;
    display: flex; align-items: center; justify-content: center; gap: 16px;
  }
  .brand-mark {
    width: 18px; height: 18px; background: var(--teal); flex: none;
  }
  .back-brand .brand-name {
    color: var(--white); font-weight: 800; font-size: 44px;
    letter-spacing: 1px; text-transform: uppercase;
  }
  .back-website {
    position: absolute; right: 40px; top: 298px;
    color: var(--white); font-size: 18px; font-weight: 500;
  }
  .back-website strong { font-weight: 700; }

  /* Front */
  .holder-name {
    position: absolute; right: 46px; top: 62px;
    color: var(--teal); font-weight: 800; font-size: 32px; line-height: 40px;
    text-transform: uppercase; letter-spacing: 0.5px;
  }
  .rule {
    position: absolute; height: 2px; background: var(--soft-white);
  }
  .rule--name { left: 400px; right: 40px; top: 112px; }
  .front-brand {
    position: absolute; left: 50px; top: 148px;
    display: flex; align-items: center; gap: 12px;
  }
  .front-brand .brand-name {
    color: var(--white); font-weight: 800; font-size: 28px; line-height: 34px;
    text-transform: uppercase; letter-spacing: 0.5px;
  }
  .rule--details { left: 40px; width: 370px; top: 228px; }
  .details {
    position: absolute; left: 44px; top: 240px;
    color: var(--white); font-size: 16px; font-weight: 400; line-height: 24px;
    list-style: none;
  }
  .details li { display: flex; align-items: center; gap: 10px; }
  .details svg { width: 14px; height: 14px; flex: none; }
  .details .web strong { color: var(--teal); font-weight: 700; }
</style>
</head>
<body>

<section class="card card--back" aria-label="Card back">
  <svg class="card-bands" viewBox="0 0 700 400" preserveAspectRatio="none">
    <polygon points="0,345 310,322 350,338 330,400 0,400" fill="var(--teal)"/>
    <polygon points="350,338 700,328 700,339 346,350" fill="var(--white)"/>
  </svg>
  <div class="back-brand">
    <span class="brand-mark"></span>
    <span class="brand-name">Harlow Estates</span>
  </div>
  <p class="back-website">www.<strong>harlowestates</strong>.com.au</p>
</section>

<section class="card card--front" aria-label="Card front">
  <svg class="card-bands" viewBox="0 0 700 400" preserveAspectRatio="none">
    <polygon points="470,300 700,290 700,350 455,360" fill="var(--teal)"/>
    <polygon points="0,375 455,360 700,350 700,362 455,372 0,388" fill="var(--white)"/>
  </svg>
  <h1 class="holder-name">Tom Harlow</h1>
  <div class="rule rule--name"></div>
  <div class="front-brand">
    <span class="brand-mark"></span>
    <span class="brand-name">Harlow Estates</span>
  </div>
  <div class="rule rule--details"></div>
  <ul class="details">
    <li>Level 2, 17 Kestrel Rd</li>
    <li>Wendale NSW 2081</li>
    <li>
      <svg viewBox="0 0 24 24" aria-hidden="true"><path fill="var(--teal)" d="M6.6 10.8a15.1 15.1 0 0 0 6.6 6.6l2.2-2.2a1 1 0 0 1 1-.25 11.4 11.4 0 0 0 3.6.6 1 1 0 0 1 1 1V20a1 1 0 0 1-1 1A17 17 0 0 1 3 4a1 1 0 0 1 1-1h3.5a1 1 0 0 1 1 1c0 1.250.2 2.45.6 3.6a1 1 0 0 1-.25 1z"/></svg>
      0437 216 590
    </li>
    <li>
      <svg viewBox="0 0 24 24" aria-hidden="true"><rect x="2" y="5" width="20" height="14" rx="2" fill="none" stroke="var(--teal)" stroke-width="2"/><path d="M3 6l9 7 9-7" fill="none" stroke="var(--teal)" stroke-width="2"/></svg>
      tom@harlowestates.com.au
    </li>
    <li class="web">
      <svg viewBox="0 0 24 24" aria-hidden="true"><circle cx="12" cy="12" r="9.5" fill="none" stroke="var(--teal)" stroke-width="2"/><ellipse cx="12" cy="12" rx="4" ry="9.5" fill="none" stroke="var(--teal)" stroke-width="2"/><path d="M2.5 12h19" stroke="var(--teal)" stroke-width="2"/></svg>
      <span>www.<strong>harlowestates</strong>.com.au</span>
    </li>
  </ul>
</section>

</body>
</html>
```